Essential oil label for bottles

Looking to modify our current logo and label design. It looks too simple. I will attach images of our competitors to use as examples. Our company name is Velnora. We have 2 different bottles. Clear and amber color. Going forward, we will be using only the amber bottle. The other 2 images are the biggest sellers brands. We want to make some adjustments to ours.

Target Market(s)

Brindex sales

Industry/Entity Type

Essential oil, perfume

Colors

Designer to choose only greyscale colors for use in the design.

Requirements
Nice to have
• A slight change to fonts and logo design. Maybe change the font and design of the word "Velnora" in our logo. Maybe add something to the label to make it stand out more but still keeping it clean and modern
Should not have
• No colors, besides, black, grays, whites, and off white.

```html
<!DOCTYPE html>
<html lang="en">
<head>
<meta charset="UTF-8">
<title>Velnora White Tea Fragrance Oil Label</title>
<link href="https://fonts.googleapis.com/css2?family=Bodoni+Moda:opsz,wght@6..96,600&family=Poppins:wght@300;400;500&display=swap" rel="stylesheet">
<style>
  :root {
    --backdrop: #d6d6d6;
    --label-black: #000000;
    --label-white: #ffffff;
    --shadow: rgba(0, 0, 0, 0.28);
  }
  * { margin: 0; padding: 0; box-sizing: border-box; }
  html, body {
    width: 1200px;
    height: 771px;
    overflow: hidden;
    background: var(--backdrop);
  }
  .canvas {
    position: relative;
    width: 1200px;
    height: 771px;
  }
  .label {
    position: absolute;
    left: 357px;
    top: 28px;
    width: 486px;
    height: 715px;
    background: var(--label-black);
    color: var(--label-white);
    box-shadow: 6px 6px 10px var(--shadow);
    font-family: "Poppins", sans-serif;
    overflow: hidden;
  }
  .brand {
    position: absolute;
    top: 96px;
    left: 0;
    width: 100%;
    text-align: center;
    font-weight: 500;
    font-size: 34px;
    letter-spacing: 9px;
    text-indent: 9px;
    line-height: 44px;
  }
  .product-name {
    position: absolute;
    top: 252px;
    left: 0;
    width: 100%;
    display: flex;
    justify-content: center;
    font-family: "Bodoni Moda", serif;
    font-weight: 600;
    font-size: 112px;
    line-height: 124px;
    white-space: nowrap;
  }
  .product-name-text {
    display: inline-block;
    flex: none;
    transform: scaleX(0.5);
    transform-origin: center;
  }
  .product-type {
    position: absolute;
    top: 366px;
    left: 0;
    width: 100%;
    text-align: center;
    font-weight: 400;
    font-size: 35px;
    line-height: 44px;
    letter-spacing: 0.5px;
  }
  .divider {
    position: absolute;
    left: 44px;
    width: 397px;
    height: 2px;
    background: var(--label-white);
  }
  .divider-top { top: 459px; }
  .divider-bottom { top: 516px; }
  .notes {
    position: absolute;
    top: 474px;
    left: 0;
    width: 100%;
    display: flex;
    justify-content: center;
    gap: 18px;
    font-weight: 400;
    font-size: 18.5px;
    line-height: 30px;
  }
  .volume {
    position: absolute;
    top: 574px;
    left: 0;
    width: 100%;
    text-align: center;
    font-weight: 400;
    font-size: 21px;
    line-height: 30px;
  }
</style>
</head>
<body>
  <main class="canvas">
    <section class="label">
      <div class="brand">VELNORA</div>
      <h1 class="product-name"><span class="product-name-text">WHITE TEA</span></h1>
      <div class="product-type">FRAGRANCE OIL</div>
      <div class="divider divider-top"></div>
      <div class="notes">
        <span>White Tea</span><span>|</span><span>Orange</span><span>|</span><span>Palo Santo</span>
      </div>
      <div class="divider divider-bottom"></div>
      <div class="volume">200ML</div>
    </section>
  </main>
</body>
</html>
```